Company or website name
- Comedy Juggler Website
- I am a Comedy/Technical Juggler, working for cruise lines, corporate events, and festivals around the world

```html
<!DOCTYPE html>
<html lang="en">
<head>
<meta charset="utf-8">
<title>Miles Tumbler – Comedy Juggler</title>
<link href="https://fonts.googleapis.com/css2?family=Arimo:wght@400;700&display=swap" rel="stylesheet">
<style>
  :root {
    --nav-dark: #262626;
    --nav-mid: #3a3a3a;
    --stage-deep: #061a4d;
    --stage-bright: #1e4aa8;
    --content-edge: #c9c9c9;
    --text-dark: #1a1a1a;
    --client-text: #333333;
    --frame-grey: #c8c8c8;
    --frame-border: #8a8a8a;
    --footer-dark: #1b1b1b;
    --white: #ffffff;
  }
  * { margin: 0; padding: 0; box-sizing: border-box; }
  html, body { width: 1200px; height: 847px; overflow: hidden; }
  body { font-family: "Arimo", Arial, sans-serif; background: var(--footer-dark); position: relative; }

  .site-nav {
    position: absolute; left: 0; top: 0; width: 1200px; height: 72px;
    background: linear-gradient(180deg, var(--nav-mid), var(--nav-dark));
    z-index: 3;
  }
  .site-nav ul { list-style: none; position: absolute; top: 25px; left: 0; width: 100%; }
  .site-nav li { position: absolute; color: var(--white); font-size: 18px; white-space: nowrap; }

  .stage {
    position: absolute; left: 0; top: 70px; width: 1200px; height: 285px;
    background: radial-gradient(ellipse 70% 90% at 50% 35%, var(--stage-bright), var(--stage-deep) 85%);
  }
  .brand-name {
    position: absolute; left: 182px; top: 66px; width: 406px;
    color: var(--white); font-size: 58px; font-weight: 700; line-height: 1; text-align: center;
    white-space: nowrap;
  }
  .brand-tagline {
    position: absolute; left: 182px; top: 196px; width: 406px; text-align: right;
    padding-right: 26px;
    color: var(--white); font-size: 17px; white-space: nowrap;
  }
  .hero-photo {
    position: absolute; left: 624px; top: 32px; width: 384px; height: 253px;
    background: linear-gradient(180deg, #2a3d6b, #55586a 60%, #2c2c30);
    border-radius: 120px 120px 0 0;
  }

  .content {
    position: absolute; left: 0; top: 355px; width: 1200px; height: 379px;
    background: radial-gradient(ellipse 55% 80% at 50% 45%, var(--white) 60%, var(--content-edge));
  }
  .intro-title { position: absolute; left: 168px; top: 18px; font-size: 34px; font-weight: 400; color: var(--text-dark); white-space: nowrap; }
  .intro-text {
    position: absolute; left: 170px; top: 66px; width: 437px;
    font-size: 17px; line-height: 21.8px; text-align: justify; color: var(--text-dark);
  }
  .video-frame {
    position: absolute; left: 647px; top: 15px; width: 377px; height: 217px;
    background: var(--frame-grey); border: 1px solid var(--frame-border);
  }
  .video-still {
    position: absolute; left: 10px; top: 9px; width: 353px; height: 199px;
    background: radial-gradient(ellipse at 50% 55%, #3a3530, #100d0b 70%);
  }
  .play-button { position: absolute; left: 151px; top: 75px; width: 50px; height: 50px; }

  .clients-title { position: absolute; left: 166px; top: 267px; font-size: 24px; font-weight: 400; color: var(--text-dark); }
  .client {
    position: absolute; top: 312px; transform: translateX(-50%);
    font-size: 17px; font-weight: 700; color: var(--client-text); white-space: nowrap;
  }

  .site-footer {
    position: absolute; left: 0; top: 734px; width: 1200px; height: 113px;
    background: var(--footer-dark); color: var(--white); text-align: center;
  }
  .footer-links { margin-top: 11px; font-size: 17px; }
  .copyright { margin-top: 5px; font-size: 17px; }
</style>
</head>
<body>
  <nav class="site-nav">
    <ul>
      <li style="left:160px">HOME</li>
      <li style="left:244px">BIOGRAPHY</li>
      <li style="left:385px">WORKSHOPS</li>
      <li style="left:539px">MEDIA CLIPS</li>
      <li style="left:683px">PROMO MATERIAL</li>
      <li style="left:873px">BOOKING INFO</li>
    </ul>
  </nav>

  <header class="stage" role="img" aria-label="Blue stage curtain backdrop">
    <div class="brand-name">Miles Tumbler</div>
    <div class="brand-tagline">Australia's Comedy Juggling Superstar</div>
    <div class="hero-photo" role="img" aria-label="Photo of the juggler holding two axes in front of the curtain"></div>
  </header>

  <main class="content">
    <h1 class="intro-title">A Night of Quirky Mayhem</h1>
    <p class="intro-text">Miles Tumbler is Australia's Newest Comedy Sensa&shy;tion. At the tender age of 23, Miles Tumbler is one of Australia's most sought after entertainers. A 45 minute spectacular of belly laughs, stupid dancing, useless skills, and contorted ideas add up to a great fun show for all! This website is still under construction, Every&shy;thing will be up and working in due time.</p>

    <div class="video-frame">
      <div class="video-still" role="img" aria-label="Video still of the juggler performing on stage">
        <svg class="play-button" viewBox="0 0 50 50">
          <circle cx="25" cy="25" r="23" fill="#1f5fc4" stroke="#e8eef8" stroke-width="3"/>
          <path d="M19 15 L35 25 L19 35 Z" fill="#ffffff"/>
        </svg>
      </div>
    </div>

    <h2 class="clients-title">Clients</h2>
    <span class="client" style="left:314px">Bluegate</span>
    <span class="client" style="left:460px">Pantryfield</span>
    <span class="client" style="left:576px">Goldbun</span>
    <span class="client" style="left:665px">Torvano</span>
    <span class="client" style="left:750px">Bavaro</span>
    <span class="client" style="left:866px">Larkin</span>
  </main>

  <footer class="site-footer">
    <p class="footer-links">Home | Biography | Workshops | Media Clips | Promo Material | Booking Info</p>
    <p class="copyright">Copyrights@milestumbler.com</p>
  </footer>
</body>
</html>
```